Business Card Design Project for Investment Fund

Orvanel Asset Partners is an emerging wealth management firm based in New Jersey. It offers superior investment returns to high net worth individuals and institutions by finding undervalued assets.
We recently selected a company logo which was inspired by the Tucana constellation. Beta Tucanae is a group of six stars, containing star cluster 47 Tucanae, rated the second brightest object in the sky.
Now we need a business card design. Since we are an investment firm, the design should project a sense of stability, growth and professionalism. The owner is interested in something simple yet striking, which of course is consistent with the logo.
Target Market(s)
Wealthy individuals, probably middle aged or older, in the US
Industry/Entity Type
Investment

```html
<!DOCTYPE html>
<html lang="en">
<head>
<meta charset="utf-8">
<title>Orvanel Asset Partners – Business Card</title>
<link href="https://fonts.googleapis.com/css2?family=Exo+2:wght@700&family=Open+Sans:wght@400;600&display=swap" rel="stylesheet">
<style>
  :root {
    --backdrop: #dcdcdc;
    --card-light: #ffffff;
    --card-dark: #2f3a42;
    --brand-blue: #1b3fa6;
    --mark-blue: #1c2f9a;
    --ink: #3a3f44;
    --ink-soft: #555b60;
    --paper-text: #ffffff;
  }
  * { margin: 0; padding: 0; box-sizing: border-box; }
  html, body {
    width: 1200px; height: 900px; overflow: hidden;
    background: var(--backdrop);
    font-family: "Open Sans", Arial, sans-serif;
  }
  .canvas { position: relative; width: 1200px; height: 900px; }
  .card {
    position: absolute; width: 590px; height: 341px;
    box-shadow: 0 2px 6px rgba(0,0,0,0.18);
  }
  .card--front { left: 167px; top: 75px; background: var(--card-light); }
  .card--back  { left: 444px; top: 484px; background: var(--card-dark); }

  .brand { position: absolute; display: flex; flex-direction: column; align-items: center; }
  .brand__square {
    background: linear-gradient(160deg, #2540b8, var(--mark-blue) 60%, #16207a);
    border-radius: 10px;
  }
  .brand__name {
    margin-top: 10px; text-align: center;
    font-weight: 600; font-size: 19px; line-height: 1.2;
    text-transform: uppercase; letter-spacing: 2px;
  }
  .card--front .brand { left: 33px; top: 98px; width: 180px; }
  .card--front .brand__square { width: 88px; height: 88px; }
  .card--front .brand__name { color: var(--ink); }
  .card--back .brand { left: 195px; top: 107px; width: 200px; }
  .card--back .brand__square { width: 78px; height: 78px; }
  .card--back .brand__name { color: var(--paper-text); }

  .holder { position: absolute; right: 43px; top: 98px; text-align: right; }
  .holder__name {
    font-family: "Exo 2", Arial, sans-serif; font-weight: 700;
    font-size: 21px; color: var(--brand-blue); letter-spacing: 0.5px;
  }
  .holder__title { font-size: 15px; color: var(--ink-soft); margin-top: 2px; }

  .address {
    position: absolute; right: 43px; top: 181px; text-align: right;
    font-size: 14px; line-height: 20px; color: var(--ink); font-style: normal;
  }
  .contacts { position: absolute; right: 41px; top: 238px; list-style: none; }
  .contacts__item {
    display: flex; justify-content: flex-end; align-items: center; gap: 8px;
    font-size: 14px; color: var(--ink); height: 23.5px;
  }
  .contacts__icon { width: 15px; height: 15px; flex: none; }

  .card__url {
    position: absolute; left: 0; right: 0; top: 300px; text-align: center;
    font-size: 15px; color: var(--paper-text);
  }
</style>
</head>
<body>
<main class="canvas">
  <section class="card card--front" aria-label="Card front">
    <div class="brand">
      <div class="brand__square"></div>
      <p class="brand__name">Orvanel<br>Asset Partners</p>
    </div>
    <div class="holder">
      <h1 class="holder__name">Daniel Harrow</h1>
      <p class="holder__title">CEO</p>
    </div>
    <address class="address">48 Mercer Ave<br>Newark, NJ 07102</address>
    <ul class="contacts">
      <li class="contacts__item">201 - 555 - 0148
        <svg class="contacts__icon" viewBox="0 0 16 16"><rect x="4" y="1" width="8" height="14" rx="1.5" fill="var(--brand-blue)"/><rect x="5.5" y="3.5" width="5" height="5" fill="#fff"/></svg>
      </li>
      <li class="contacts__item">dharrow@orvanelpartners.com
        <svg class="contacts__icon" viewBox="0 0 16 16"><rect x="1" y="3" width="14" height="10" fill="none" stroke="var(--brand-blue)" stroke-width="1.6"/><path d="M1 3l7 6 7-6M1 13l5-4.5M15 13l-5-4.5" fill="none" stroke="var(--brand-blue)" stroke-width="1.4"/></svg>
      </li>
      <li class="contacts__item">www.orvanelpartners.com
        <svg class="contacts__icon" viewBox="0 0 16 16"><circle cx="8" cy="8" r="6.5" fill="none" stroke="var(--brand-blue)" stroke-width="1.6"/><ellipse cx="8" cy="8" rx="3" ry="6.5" fill="none" stroke="var(--brand-blue)" stroke-width="1.2"/><path d="M1.5 8h13M2.5 5h11M2.5 11h11" stroke="var(--brand-blue)" stroke-width="1.1"/></svg>
      </li>
    </ul>
  </section>

  <section class="card card--back" aria-label="Card back">
    <div class="brand">
      <div class="brand__square"></div>
      <p class="brand__name">Orvanel<br>Asset Partners</p>
    </div>
    <p class="card__url">www.orvanelpartners.com</p>
  </section>
</main>
</body>
</html>
```